SunGrove Yoga Website Design

Business Logo - attached
5 pages being:
Home
About
Classes
Blog
Contact

Would like Scrolling webpage and yoga symbols to be used.

Must have's being:
Easy to navigate, Text needs to be able to be edited/updated, Enquire Now Links, More Information Links, be a secure site, SEO,

Please refer to attached document for the information for the body of the website.

Target Market(s)

Educators, Community Service, Health and Wellbeing, Mental Health

Industry/Entity Type

Yoga

Coding

Coded - Design and coding required

Number of Pages Required

5+ page

Font styles to use
Other font styles liked:
• Bella Bold BC

Colors
0094D4
00A9DD
6FCCEA
C7EBF8
E9F6FB
6B429C
8869AF
B7A5CE
E3DAEB
F3F0F8

Requirements
Must have
• Easy to navigate, Text needs to be able to be edited/updated, Enquire Now Links, More Information Links, be a secure site, SEO,
Nice to have
• Scrolling webpage, yoga symbols

```html
<!DOCTYPE html>
<html lang="en">
<head>
<meta charset="utf-8">
<title>SunGrove Yoga – Home</title>
<link href="https://fonts.googleapis.com/css2?family=Kaushan+Script&family=Poppins:wght@400;500;600&display=swap" rel="stylesheet">
<style>
:root{
  --blue:#0094D4;--blue-2:#00A9DD;--blue-3:#6FCCEA;--blue-4:#C7EBF8;--blue-5:#E9F6FB;
  --purple:#6B429C;--purple-2:#8869AF;--purple-3:#B7A5CE;--purple-4:#E3DAEB;--purple-5:#F3F0F8;
  --teal:#1f8ea8;--navy:#142a3f;--ink:#1e2235;--text:#3a3d4a;--forest:#1f3b33;--paper:#f1efe3;
}
*{margin:0;padding:0;box-sizing:border-box}
html,body{width:1200px;height:4319px;overflow:hidden}
body{position:relative;background:#fff;font-family:'Poppins',sans-serif;color:var(--text)}
.abs{position:absolute}
.script{font-family:'Kaushan Script',cursive;color:var(--ink);font-weight:400}
.ph{position:absolute}
.brush-btn{position:absolute;display:flex;align-items:center;justify-content:center;color:#fff;font-weight:600;font-size:16px;letter-spacing:.5px;background:var(--teal);
  clip-path:polygon(2% 12%,20% 4%,45% 10%,70% 2%,98% 8%,100% 40%,97% 60%,100% 88%,75% 96%,50% 90%,25% 98%,3% 92%,0 60%,3% 35%)}
/* nav */
.nav-mark{left:174px;top:10px;display:flex;align-items:center;gap:10px}
.nav-mark .dot{width:40px;height:40px;border-radius:50%;background:var(--navy)}
.nav-mark span{font-size:15px;font-weight:600;color:var(--navy)}
.nav a{position:absolute;top:35px;font-size:15px;color:var(--ink);text-decoration:none}
.nav a.active{color:var(--purple-2)}
/* hero */
.hero-band{left:0;top:0}
.hero h1{position:absolute;left:176px;top:205px;font-size:38px}
.hero p{position:absolute;left:176px;top:278px;width:480px;font-size:14px;line-height:22px;color:var(--ink)}
/* about */
.about h2{position:absolute;left:637px;top:650px;font-size:32px}
.about p{position:absolute;left:637px;width:380px;font-size:14px;line-height:20.5px;color:var(--ink)}
.section-title{position:absolute;width:1200px;text-align:center;font-size:32px}
.underline{position:absolute;height:4px;border-radius:3px;background:var(--navy)}
/* blog */
.blog-card{left:213px;top:2460px;width:416px;height:381px;background:#f6f6f6}
.blog-frame{left:639px;top:2423px;width:352px;height:457px;border:3px solid var(--navy);border-radius:3px}
.tag{left:230px;top:2520px;width:98px;height:28px;border-radius:14px;background:var(--purple-2);color:#fff;font-size:14px;display:flex;align-items:center;justify-content:center}
.blog-title{left:230px;top:2558px;width:400px;font-size:26px;line-height:37px;color:var(--ink);font-weight:500}
.blog-text{left:230px;top:2650px;width:390px;font-size:13px;line-height:21px;color:var(--ink)}
.read-more{left:230px;top:2724px;font-size:13px;color:var(--blue)}
.meta{left:230px;top:2760px;font-size:13px;color:var(--ink);display:flex;gap:22px;align-items:center}
.meta i{display:inline-block;width:12px;height:12px;border:1.5px solid #888;border-radius:2px;margin-right:8px;vertical-align:-1px}
.arrow-btn{width:26px;height:26px;border-radius:50%;border:1.5px solid var(--blue-2);display:flex;align-items:center;justify-content:center}
/* find out */
.find{left:0;top:2938px;width:1200px;height:486px;background:linear-gradient(100deg,#183229 0%,#2b4a3e 45%,#1d3b33 100%)}
.find h2{position:absolute;left:172px;top:3008px;font-size:40px;color:#fff}
.find-text{left:172px;width:400px;color:#fff;font-size:14px;line-height:20.5px}
.find-phone{left:172px;top:3240px;font-size:40px;font-weight:500;color:#fff}
.form-card{left:654px;top:3002px;width:370px;height:476px;background:#fff;box-shadow:0 4px 14px rgba(0,0,0,.18);border-radius:3px}
.form-card h3{position:absolute;width:370px;text-align:center;top:22px;font-size:26px}
.field{position:absolute;left:20px;width:332px;height:44px;background:#efefef;border-radius:8px;font-size:12px;color:#888;padding:14px 18px}
.submit{position:absolute;left:20px;top:377px;width:332px;height:46px;background:var(--purple-2);color:#fff;border-radius:8px;font-weight:600;font-size:15px;display:flex;align-items:center;justify-content:center}
/* contact */
.contact h2{position:absolute;left:469px;top:3572px;font-size:38px}
.c-row{position:absolute;left:479px;display:flex;align-items:center;gap:16px;font-size:14px;color:var(--ink)}
.c-row svg{width:18px;height:18px}
/* footer */
.footer{left:0;top:4106px;width:1200px;height:213px;background:var(--navy)}
.foot-badge{left:176px;top:4023px;width:194px;height:194px;border-radius:50%;background:var(--navy);border:4px solid #fff;display:flex;align-items:center;justify-content:center;color:#fff;font-size:20px;font-weight:500}
.foot-h{font-family:'Kaushan Script',cursive;color:#fff;font-size:13px;letter-spacing:1.5px}
.soc{width:28px;height:28px;border-radius:50%;background:var(--purple-2)}
.news{left:726px;top:4205px;width:298px;height:29px;border-radius:15px;background:#fff;font-size:12px;color:var(--ink);padding:6px 14px}
.news .send{position:absolute;right:8px;top:4px;width:22px;height:22px;border-radius:50%;background:var(--purple-3)}
.copy{left:0;top:4282px;width:1200px;text-align:center;color:#fff;font-size:11px}
</style>
</head>
<body>

<!-- Hero -->
<svg class="abs hero-band" width="1200" height="600" viewBox="0 0 1200 600" aria-hidden="true">
  <path d="M0 0H1200V532C1080 548 960 520 820 528C640 540 520 505 330 520C180 532 80 560 0 595Z" fill="#e5dcee"/>
</svg>
<div class="ph" role="img" aria-label="Faint mandala pattern" style="left:880px;top:0;width:320px;height:320px;border-radius:50%;background:radial-gradient(circle,rgba(183,165,206,.25),rgba(227,218,235,0) 70%)"></div>
<div class="ph" role="img" aria-label="White lotus flowers and seed pods" style="left:0;top:150px;width:250px;height:395px;background:linear-gradient(180deg,rgba(255,255,255,0) 0%,rgba(245,242,248,.9) 60%,rgba(255,255,255,.95) 100%);border-radius:0 60% 40% 0"></div>
<div class="ph" role="img" aria-label="Woman in purple top holding a twisted side plank pose on a yoga mat" style="left:503px;top:160px;width:654px;height:318px;background:linear-gradient(160deg,#d9cde6 0%,#8a5ba8 40%,#7c7a84 70%,#6f6d78 100%);border-radius:40% 20% 10% 30%;opacity:.85"></div>

<header class="nav">
  <div class="abs nav-mark"><div class="dot"></div><span>SunGrove Yoga</span></div>
  <a class="active" style="left:576px">Home</a>
  <a style="left:659px">About</a>
  <a style="left:742px">Classes</a>
  <a style="left:838px">Blog</a>
  <a style="left:910px">Contact</a>
  <svg class="abs" style="left:1008px;top:37px" width="16" height="16" viewBox="0 0 16 16" fill="none" stroke="#1e2235" stroke-width="1.6"><circle cx="7" cy="7" r="5"/><path d="M11 11l4 4"/></svg>
</header>

<section class="hero">
  <h1 class="script">Welcome to SunGrove Yoga...</h1>
  <p>SunGrove Yoga believe that you are never too young to benefit from and fall in love with yoga.</p>
  <a class="brush-btn" style="left:181px;top:347px;width:235px;height:45px">Read More</a>
</section>

<!-- About -->
<section class="about">
  <div class="ph" style="left:179px;top:615px;width:128px;height:128px;border-radius:50%;border:16px solid var(--blue-4)"></div>
  <div class="ph" style="left:172px;top:876px;width:108px;height:108px;border-radius:50%;background:var(--purple-3)"></div>
  <div class="ph" role="img" aria-label="Person meditating on a rock by a misty lake" style="left:196px;top:662px;width:318px;height:318px;border-radius:50%;border:3px solid var(--purple);background:linear-gradient(180deg,#c9d3dc 0%,#9aa9b4 45%,#6c7880 70%,#4a5258 100%)"></div>
  <div class="ph" role="img" aria-label="Woman meditating in a sunlit room" style="left:424px;top:829px;width:168px;height:168px;border-radius:50%;border:3px solid var(--purple);background:linear-gradient(135deg,#f1c27a 0%,#c98b4a 50%,#7a5136 100%)"></div>
  <div class="ph" role="img" aria-label="Faint butterflies and meditating figure" style="left:650px;top:580px;width:160px;height:110px;background:radial-gradient(circle,rgba(183,165,206,.25),rgba(255,255,255,0) 70%)"></div>
  <h2 class="script">About Us</h2>
  <p style="top:712px">My aim is to EMPOWER kids and teens to thrive by teaching life skills in Yoga, Mindfulness and Breathing techniques to deal with daily challenges and big emotions.</p>
  <p style="top:804px">SunGrove Yoga gives kids an opportunity to enjoy and experience yoga for themselves and primarily focuses on programs for Schools, Pre Schools and Early Learning Centres.</p>
  <a class="brush-btn" style="left:640px;top:910px;width:240px;height:48px">Know More</a>
</section>

<!-- Classes -->
<h2 class="script section-title" style="top:1082px">Our Classes</h2>
<div class="underline" style="left:537px;top:1132px;width:128px"></div>
<div class="ph" role="img" aria-label="Faint mandala pattern behind classes" style="left:230px;top:1230px;width:740px;height:740px;border-radius:50%;background:radial-gradient(circle,rgba(227,218,235,.35),rgba(255,255,255,0) 65%)"></div>
<div class="ph" role="img" aria-label="Faint silhouettes of people in yoga poses" style="left:180px;top:2060px;width:840px;height:220px;background:linear-gradient(180deg,rgba(243,240,248,0) 0%,rgba(243,240,248,.9) 50%,rgba(243,240,248,0) 100%)"></div>
<div class="ph" role="img" aria-label="Woman in red meditating in front of a pink lotus flower" style="left:503px;top:1475px;width:184px;height:327px;border-radius:48% 48% 40% 40%;background:linear-gradient(180deg,#f7d9e3 0%,#f2b4c6 35%,#e9c7cf 50%,#b8253a 80%,#9b1d30 100%)"></div>

<svg class="abs" style="left:0;top:1156px" width="1200" height="985" viewBox="0 690 716 588" font-family="Poppins, sans-serif" fill="#1e2235">
  <g fill="none" stroke-width="1.6">
    <polygon points="328,708 413,752 413,843 330,880" stroke="#B7A5CE"/>
    <polygon points="108,852 195,815 262,850 258,950" stroke="#a9c6d6"/>
    <polygon points="433,905 586,824 586,920 515,962" stroke="#3fa3d0"/>
    <polygon points="128,1045 200,1008 280,1062 128,1143" stroke="#8869AF"/>
    <polygon points="457,1015 611,1100 530,1148 457,1108" stroke="#8869AF"/>
    <polygon points="294,1108 380,1090 380,1262 294,1215" stroke="#0094D4"/>
    <polyline points="322,845 276,922 262,945" stroke="#B7A5CE"/>
    <polyline points="317,862 285,930" stroke="#6FCCEA"/>
    <polyline points="366,888 430,888 440,900 520,900" stroke="#0094D4"/>
    <polyline points="378,896 425,896 436,910" stroke="#6FCCEA"/>
    <polyline points="445,945 476,1000 460,1030" stroke="#8869AF"/>
    <polyline points="455,950 470,985" stroke="#B7A5CE"/>
    <polyline points="248,955 238,968 265,1030 280,1045" stroke="#6FCCEA"/>
    <polyline points="276,1055 290,1082 365,1082" stroke="#8869AF"/>
    <polyline points="440,1022 400,1090 380,1092" stroke="#0094D4"/>
    <polyline points="436,1040 410,1070" stroke="#00A9DD"/>
  </g>
  <polygon points="292,728 323,710 323,745" fill="#d7c8ec"/>
  <polygon points="103,865 133,880 103,898" fill="#C7EBF8"/>
  <polygon points="550,803 580,820 550,837" fill="#6FCCEA"/>
  <polygon points="135,1148 165,1128 165,1165" fill="#B7A5CE"/>
  <polygon points="583,1078 612,1060 612,1096" fill="#8869AF"/>
  <polygon points="384,1225 414,1242 384,1258" fill="#00A9DD"/>
  <g text-anchor="middle" font-size="5.2">
    <text x="370" y="771" font-size="8" font-weight="600">Private Sessions</text>
    <text x="370" y="788">if they would benefit</text><text x="370" y="798">from an individualised</text><text x="370" y="808">program to suit their</text><text x="370" y="818">needs, then you can</text><text x="370" y="828">consider a private</text><text x="370" y="838">lesson.</text>
    <text x="187" y="861" font-size="8" font-weight="600">Yoga for Tweens (aged 7–11)</text>
    <text x="217" y="877">An interactive 60-minute</text><text x="217" y="887">class for children aged</text><text x="217" y="897">7–11 to enjoy yoga</text><text x="217" y="907">poses; games</text>
    <text x="535" y="889" font-size="8" font-weight="600">Yoga for Teen Girls</text>
    <text x="534" y="905">If your daughter is not yet a</text><text x="534" y="915">teen, but is in high</text><text x="534" y="925">school, she can join.</text>
    <text x="192" y="1056" font-size="8" font-weight="600">Yoga in Early Learning</text>
    <text x="191" y="1073">Offer SunGrove Yoga at your</text><text x="191" y="1083">childcare centre or</text><text x="191" y="1093">Kindergarten.</text>
    <text x="502" y="1072" font-size="8" font-weight="600">Kids Yoga Online</text>
    <text x="514" y="1089">'Online' is the new world</text><text x="514" y="1099">we live in and whilst it</text><text x="514" y="1109">is not my favourite</text><text x="514" y="1119">way to connect, it is</text>
    <text x="338" y="1144" font-size="8" font-weight="600">Yoga in Schools</text>
    <text x="338" y="1161">Offer SunGrove Yoga</text><text x="338" y="1171">at your school!</text><text x="338" y="1181">Classes are tailored</text><text x="338" y="1191">by the age of</text><text x="338" y="1201">students.</text>
  </g>
</svg>
<a class="brush-btn" style="left:481px;top:2155px;width:235px;height:46px">Explore All</a>

<!-- Blogs -->
<h2 class="script section-title" style="top:2317px">Our Blogs</h2>
<div class="underline" style="left:548px;top:2366px;width:110px"></div>
<div class="abs blog-frame"></div>
<div class="abs blog-card"></div>
<div class="ph" role="img" aria-label="Man practising a headstand on a mat outdoors" style="left:629px;top:2400px;width:343px;height:419px;background:linear-gradient(180deg,#7fb4e3 0%,#b9d6ee 35%,#8a9a6a 60%,#b08d62 85%,#a2805a 100%)"></div>
<div class="abs tag">Hatha</div>
<div class="abs blog-title">Become an Yoga trainer at Yogi center.</div>
<div class="abs blog-text">Yoga is a physical, mental, and spiritual practice or discipline. There is a broad variety of schools, practices and goals in Hinduism, Buddhism. The origins...</div>
<div class="abs read-more">Read More »</div>
<div class="abs meta"><span><i></i>April 16, 2015</span><span><i style="border-radius:50%"></i>9:00 - 11:00</span><span><i></i>1 Comment</span></div>
<div class="abs arrow-btn" style="left:176px;top:2625px"><svg width="10" height="10" viewBox="0 0 10 10" fill="none" stroke="#00A9DD" stroke-width="1.5"><path d="M6.5 1.5L3 5l3.5 3.5"/></svg></div>
<div class="abs arrow-btn" style="left:1003px;top:2625px;background:var(--blue-5)"><svg width="10" height="10" viewBox="0 0 10 10" fill="none" stroke="#0094D4" stroke-width="1.5"><path d="M3.5 1.5L7 5 3.5 8.5"/></svg></div>

<!-- Find out more -->
<section class="abs find" role="img" aria-label="Woman practising yoga among dark green foliage, darkened">
  <div class="ph" style="left:560px;top:0;width:400px;height:486px;background:radial-gradient(ellipse at 50% 60%,rgba(90,110,100,.35),rgba(0,0,0,0) 70%)"></div>
</section>
<h2 class="abs script" style="left:172px;top:3008px;font-size:40px;color:#fff">Find Out More...</h2>
<p class="abs find-text" style="top:3084px">If you would like any further information or simply need clarification, please send me an email and I will happily answer your questions either via email or over the phone if you prefer.</p>
<p class="abs find-text" style="top:3196px;font-weight:500">Alternatively, please call Hannah</p>
<div class="abs find-phone">0400 815 262</div>
<form class="abs form-card">
  <h3 class="script">Get In Touch</h3>
  <div class="field" style="top:77px">Name</div>
  <div class="field" style="top:144px">Email</div>
  <div class="field" style="top:209px">Subject</div>
  <div class="field" style="top:275px;height:82px">Message</div>
  <div class="submit">Submit</div>
</form>

<!-- Contact -->
<section class="contact">
  <div class="ph" role="img" aria-label="Torn sheet of cream paper" style="left:293px;top:3495px;width:687px;height:519px;background:var(--paper);clip-path:polygon(2% 4%,15% 1%,30% 5%,48% 0,66% 4%,82% 1%,98% 5%,100% 30%,97% 55%,100% 80%,96% 98%,75% 100%,55% 96%,35% 100%,15% 97%,1% 100%,3% 75%,0 50%,2% 25%)"></div>
  <div class="ph" role="img" aria-label="White feather" style="left:243px;top:3553px;width:226px;height:92px;border-radius:50%;background:radial-gradient(ellipse,rgba(220,220,220,.9),rgba(255,255,255,0) 70%)"></div>
  <div class="ph" role="img" aria-label="Stacked stones with pink frangipani and bamboo" style="left:0;top:3913px;width:201px;height:210px;border-radius:40% 40% 0 0;background:linear-gradient(180deg,#8fc66b 0%,#e88aa3 40%,#4a4a4a 75%,#2e2e2e 100%)"></div>
  <div class="ph" role="img" aria-label="Stacked stones with white frangipani and bamboo" style="left:939px;top:3788px;width:261px;height:302px;border-radius:45% 20% 0 0;background:linear-gradient(180deg,#9ccc6a 0%,#f2e8a0 35%,#7a7a7a 65%,#3a3a3a 100%)"></div>
  <h2 class="script">Contact Us</h2>
  <div class="underline" style="left:469px;top:3627px;width:96px"></div>
  <div class="c-row" style="top:3654px"><svg viewBox="0 0 18 18" fill="none" stroke="#555" stroke-width="1.3"><circle cx="9" cy="6" r="3.5"/><path d="M2.5 16c1-3.5 3.5-5 6.5-5s5.5 1.5 6.5 5"/></svg>Hannah Whitfield</div>
  <div class="c-row" style="top:3692px"><svg viewBox="0 0 18 18" fill="none" stroke="#555" stroke-width="1.3"><path d="M9 16s5-5 5-9a5 5 0 0 0-10 0c0 4 5 9 5 9z"/><circle cx="9" cy="7" r="1.8"/></svg>Wattle Bend, Victoria Australia 3790</div>
  <div class="c-row" style="top:3740px;font-size:32px;font-weight:400"><svg viewBox="0 0 18 18" fill="none" stroke="#555" stroke-width="1.3" style="width:26px;height:26px"><circle cx="9" cy="9" r="8"/><path d="M6 5l1.5-.3 1 2.3-1 1a5 5 0 0 0 2.5 2.5l1-1 2.3 1-.3 1.5c-3.5.5-7.5-3.5-7-7z"/></svg>0400 815 262</div>
  <div class="c-row" style="top:3801px"><svg viewBox="0 0 18 18" fill="none" stroke="#555" stroke-width="1.3"><circle cx="9" cy="9" r="8"/><rect x="5" y="6" width="8" height="6"/><path d="M5 6l4 3 4-3"/></svg>info@sungroveyoga.com.au</div>
  <div class="c-row" style="top:3840px"><svg viewBox="0 0 18 18" fill="none" stroke="#555" stroke-width="1.3"><circle cx="9" cy="9" r="8"/><ellipse cx="9" cy="9" rx="3.5" ry="8"/><path d="M1 9h16"/></svg>www.sungroveyoga.com.au</div>
  <div class="c-row" style="top:3879px"><svg viewBox="0 0 18 18" fill="none" stroke="#555" stroke-width="1.3"><circle cx="9" cy="9" r="8"/><circle cx="9" cy="9" r="2"/></svg>SunGrove Yoga | Social</div>
  <div class="c-row" style="top:3918px"><svg viewBox="0 0 18 18" fill="none" stroke="#555" stroke-width="1.3"><circle cx="9" cy="9" r="8"/><rect x="5" y="5" width="8" height="8" rx="2"/></svg>sungroveyoga4kids</div>
</section>

<!-- Footer -->
<footer class="abs footer"></footer>
<div class="abs foot-badge">SunGrove Yoga</div>
<div class="abs foot-h" style="left:511px;top:4168px">FOLLOW US</div>
<div class="abs soc" style="left:494px;top:4206px"></div>
<div class="abs soc" style="left:534px;top:4206px"></div>
<div class="abs soc" style="left:576px;top:4206px"></div>
<div class="abs foot-h" style="left:726px;top:4168px">SUBSCRIBE OUR NEWSLETTER</div>
<div class="abs news">Email....<span class="send"></span></div>
<div class="abs copy">Copyright 2023 SunGrove Yoga</div>

</body>
</html>
```